Stationary package for Health Care company

COMPANY NAME: Vantorel.
We have a company logo. We need to create a stationary package for a new health care company. The package needs to be unique, high tech, innovative (perhaps a folded business card, or something with a die-cut). It needs to be memorable.

The company makes in-home allergy test kits - customer takes an allergy test at home (with special medical device found in the kit) then, they send in their blood samples, and the company sends back a detailed report of what they are/are not allergic to.

We need:
business cards
thank you cards
labels
stationary
envelope
9" x 12" Pocket folder

Vantorel (The company) has a brochure for the product (called Mirodane). The stationary package should compliment the brochure. The brochure will reside in the pocket folder and they must look good together. Brochure uploaded. Note: the brochure is flat. Once folded - all you will actually see in the pocket folder is the cover with the man with outstretched arms.

INFO TO BE USED ON STATIONARY: DO NOT TRY AND CONTACT THIS PERSON!

Peter J. Harwick
Chief Executive Officer
48 Orland Commerce Parkway #210
Corvell Heights OR 97071
Phone: 503-555-0172
Web site: www.vantorel-example.com
email: pharwick@vantorel-example.com
Updates

I have added all of the information to be used on the stationary package. PLEASE DO NOT TRY TO CONTACT THIS PERSON OR COMPANY. If you have any questions - contact me. Thank you. Owen

I've uploaded a cleaned up version of the Vantorel logo as a 300 dpi PSD if anyone needs it. Thank you. Owen

Target Market(s)

Doctors, hospitals, laboratories.

Industry/Entity Type

Medical

Requirements
Must have
• Must be memorable, high-tech. Must work together with Mirodane brochure. Descriptive words: freedom, breathe, clean, fresh

```html
<!DOCTYPE html>
<html lang="en">
<head>
<meta charset="utf-8">
<title>Vantorel Business Card</title>
<link href="https://fonts.googleapis.com/css2?family=Questrial&family=Open+Sans:wght@400;700&display=swap" rel="stylesheet">
<style>
  :root {
    --backdrop: #1c1c1c;
    --card-white: #f7f7f7;
    --brand-navy: #1f2a86;
    --brand-blue: #3f5bb0;
    --brand-light: #8ea8ee;
    --brand-pale: #c9d3ee;
    --ink: #3a3a3a;
    --back-top: #2c3c98;
    --back-bottom: #141c5c;
  }
  * { margin: 0; padding: 0; box-sizing: border-box; }
  html, body { width: 1200px; height: 1000px; overflow: hidden; }
  body { background: var(--backdrop); position: relative; font-family: "Questrial", sans-serif; }

  .card { position: absolute; width: 532px; height: 303px; overflow: hidden; }

  .card-front { left: 205px; top: 163px; background: var(--card-white); }
  .front-wordmark {
    position: absolute; left: 36px; top: 56px;
    display: flex; align-items: center; gap: 10px;
    font-size: 42px; color: var(--brand-navy); letter-spacing: 0.3px; line-height: 1;
  }
  .wordmark-dot { width: 14px; height: 14px; border-radius: 50%; background: var(--brand-light); }
  .holder { position: absolute; right: 36px; top: 66px; text-align: right; }
  .holder-name {
    font-family: "Open Sans", sans-serif; font-weight: 700; font-size: 15.5px;
    color: var(--brand-blue); letter-spacing: 0.6px; text-transform: uppercase;
  }
  .holder-title { font-size: 13px; color: var(--ink); margin-top: 0; }
  .address { position: absolute; left: 49px; top: 148px; font-size: 10.5px; color: var(--ink); line-height: 18px; }
  .contact-list { position: absolute; left: 49px; top: 190px; list-style: none; font-size: 10.5px; color: var(--ink); }
  .contact-list li { display: flex; align-items: center; gap: 9px; height: 17px; }
  .contact-icon { width: 12px; height: 12px; display: block; }
  .front-wave { position: absolute; left: 0; bottom: 0; width: 532px; height: 60px; }

  .card-back {
    left: 472px; top: 549px;
    background: radial-gradient(ellipse at 40% 20%, var(--back-top) 0%, #22308a 45%, var(--back-bottom) 100%);
  }
  .back-lockup { position: absolute; left: 0; right: 0; top: 132px; text-align: center; }
  .back-wordmark {
    display: inline-flex; align-items: center; gap: 10px;
    font-size: 44px; color: var(--brand-light); letter-spacing: 0.5px; line-height: 1;
  }
  .back-wordmark .wordmark-dot { background: var(--brand-pale); }
  .tagline { margin-top: 14px; font-size: 13px; color: var(--brand-light); letter-spacing: 0.2px; }
</style>
</head>
<body>

<section class="card card-front" aria-label="Business card front">
  <div class="front-wordmark"><span class="wordmark-dot"></span><span>Vantorel</span></div>

  <div class="holder">
    <p class="holder-name">Peter J. Harwick</p>
    <p class="holder-title">Chief Executive Officer</p>
  </div>

  <p class="address">48 Orland Commerce Parkway #210<br>Corvell Heights OR 97071</p>

  <ul class="contact-list">
    <li>
      <svg class="contact-icon" viewBox="0 0 12 12" aria-hidden="true"><rect width="12" height="12" rx="2" fill="#3f5bb0"/><path d="M3.5 2.8c.4 2.8 2.6 5.2 5.6 5.9l.5-1.2-1.4-.8-.6.6C6.5 6.8 5.3 5.6 4.8 4.5l.6-.6-.8-1.4z" fill="#fff"/></svg>
      <span>503-555-0172</span>
    </li>
    <li>
      <svg class="contact-icon" viewBox="0 0 12 12" aria-hidden="true"><rect width="12" height="12" rx="2" fill="#3f5bb0"/><rect x="2.5" y="3.5" width="7" height="5" fill="none" stroke="#fff" stroke-width="0.9"/><path d="M2.5 3.5 6 6.3 9.5 3.5" fill="none" stroke="#fff" stroke-width="0.9"/></svg>
      <span>info@vantorel-example.com</span>
    </li>
    <li>
      <svg class="contact-icon" viewBox="0 0 12 12" aria-hidden="true"><rect width="12" height="12" rx="2" fill="#3f5bb0"/><circle cx="6" cy="6" r="3.4" fill="none" stroke="#fff" stroke-width="0.8"/><ellipse cx="6" cy="6" rx="1.4" ry="3.4" fill="none" stroke="#fff" stroke-width="0.8"/><path d="M2.6 6h6.8" stroke="#fff" stroke-width="0.8"/></svg>
      <span>www.vantorel-example.com</span>
    </li>
  </ul>

  <svg class="front-wave" viewBox="0 0 532 60" preserveAspectRatio="none" aria-hidden="true">
    <path d="M0 44 C120 20 260 0 532 6 L532 60 L0 60 Z" fill="#2a3590"/>
    <path d="M0 50 C150 34 300 14 532 22 L532 26 C330 22 170 40 0 58 Z" fill="#c9d3ee"/>
    <path d="M90 60 C220 36 380 22 532 30 L532 60 Z" fill="#3a4aa6"/>
    <path d="M0 44 C120 20 260 0 532 6" fill="none" stroke="#1f2a86" stroke-width="2"/>
  </svg>
</section>

<section class="card card-back" aria-label="Business card back">
  <div class="back-lockup">
    <div class="back-wordmark"><span class="wordmark-dot"></span><span>Vantorel</span></div>
    <p class="tagline">Fresh Answers For Every Breath Ahead</p>
  </div>
</section>

</body>
</html>
```